Support Welcome Packet Redesign

Looking to redesign our current "welcome packet" that we send to our new customers to help them understand our support service. It is currently in Microsoft Word and would like to remain in either word or publisher. Something that we can easily edit, as the content adjusts based on the customer needs. We want this document to be simple and understandable as it should be something our customers can reference at any time during our contract and easy to navigate.

Target Market(s)

Current Customers. Healthcare, Oil & Gas, Transportation, etc.

Industry/Entity Type

It Service

Font styles to use
Sans Serif

Requirements
Must have
• Table of Contents, exWave Logo and current content
Nice to have
• Easy navigation. Redone final page (contact info)

```html
<!DOCTYPE html>
<html lang="en">
<head>
<meta charset="utf-8">
<title>exWave Welcome Packet</title>
<link rel="stylesheet" href="https://fonts.googleapis.com/css2?family=Carlito:wght@400;700&display=swap">
<style>
:root{
  --backdrop:#ececec;
  --page:#ffffff;
  --page-edge:#c6c6c6;
  --orange:#f07c22;
  --ink:#2a2a2a;
  --muted:#666666;
  --side-green:#b5d99f;
  --greet-green-a:#5f8f2e;
  --greet-green-b:#c8deb0;
  --link:#1f3fd1;
  --brand-square:#f3a15a;
}
*{margin:0;padding:0;box-sizing:border-box}
html,body{width:1200px;height:956px;overflow:hidden;background:var(--backdrop)}
body{font-family:"Carlito",sans-serif;font-weight:400;color:var(--ink);position:relative}
.spread{position:absolute;left:302px;top:59px;display:grid;grid-template-columns:287px 287px;grid-template-rows:371px 371px;column-gap:5px;row-gap:6px}
.page{position:relative;background:var(--page);border:1px solid var(--page-edge);overflow:hidden}

.corner-brand{position:absolute;left:228px;top:14px;width:32px;display:flex;flex-direction:column;align-items:center;gap:2px;font-size:8px;color:var(--orange);line-height:1}
.corner-brand .mark{width:14px;height:14px;background:var(--brand-square);opacity:.45}

/* cover */
.cover-brand{position:absolute;left:32px;top:100px;width:64px;display:flex;flex-direction:column;align-items:center}
.cover-brand .mark{width:54px;height:54px;background:var(--brand-square)}
.cover-brand .name{font-size:18px;color:var(--orange);line-height:1;margin-top:12px}
.cover-brand .tag{font-size:5px;color:var(--muted);margin-top:2px}
.welcome{position:absolute;left:114px;top:123px;font-size:15px;color:var(--orange)}
.greetings{position:absolute;left:176px;top:157px;width:78px;height:176px;background:linear-gradient(180deg,var(--greet-green-a),var(--greet-green-b));opacity:.5}

/* contents */
.toc-title{position:absolute;left:41px;top:83px;font-size:12px;font-weight:400;color:var(--orange)}
.toc{position:absolute;left:41px;top:109px;width:213px;list-style:none;font-size:5.3px;color:var(--ink)}
.toc li{display:flex;align-items:baseline;height:14.3px}
.toc li .lead{flex:1;border-bottom:1px dotted #888;margin:0 1px;transform:translateY(-1px)}
.toc .l2{padding-left:8px}
.toc .l3{padding-left:16px}
.footer{position:absolute;left:32px;right:32px;top:315px;display:flex;justify-content:space-between;font-size:3.2px;color:var(--muted)}
.footer .web{color:var(--link);text-decoration:underline}
.page-num{position:absolute;left:0;right:0;top:343px;text-align:center;font-size:3.2px;color:var(--muted)}

/* summary pages */
.side-label{position:absolute;font-size:10px;font-weight:700;color:var(--side-green);writing-mode:vertical-rl;transform:rotate(180deg);white-space:nowrap}
.section-title{position:absolute;font-size:10.5px;font-weight:700;color:var(--orange);text-decoration:underline}
.body-copy{position:absolute;left:41px;width:212px;font-size:5.6px;text-align:justify;color:var(--ink)}
.body-copy a{color:var(--link)}
.service-list{position:absolute;left:41px;top:145px;width:212px;list-style:none;font-size:5.6px;color:var(--ink)}
.service-list li{position:relative;padding-left:9px;height:18.2px;line-height:9px}
.service-list li::before{content:"";position:absolute;left:2px;top:3px;width:2.5px;height:2.5px;border-radius:50%;background:var(--ink)}
.service-list li.wrap{text-align:justify;line-height:14px;margin-top:-3px}
</style>
</head>
<body>
<main class="spread">

  <section class="page cover">
    <div class="cover-brand">
      <span class="mark"></span>
      <span class="name">exWave</span>
      <span class="tag">Technology Corp.</span>
    </div>
    <div class="welcome">Welcome.</div>
    <div class="greetings" role="img" aria-label="Column of hand-lettered greetings saying welcome in many languages, in shades of green"></div>
  </section>

  <section class="page contents">
    <div class="corner-brand"><span class="mark"></span>exWave</div>
    <h2 class="toc-title">Table of Contents</h2>
    <ol class="toc">
      <li>Document Summary<span class="lead"></span>3</li>
      <li><span class="lead"></span>4</li>
      <li>Services Summary<span class="lead"></span>4</li>
      <li>Support Information<span class="lead"></span>5</li>
      <li class="l2">exWave Support Teams and Escalation Path<span class="lead"></span>5</li>
      <li class="l2">exWave Support Escalation Matrix<span class="lead"></span>6</li>
      <li class="l3">Priority Level<span class="lead"></span>6</li>
      <li class="l3">Escalation Guidelines<span class="lead"></span>7</li>
      <li class="l2">exWave Support Contact Information<span class="lead"></span>8</li>
      <li class="l2">exWave Support<span class="lead"></span>9</li>
    </ol>
    <div class="footer">
      <span>exWave Technology</span>
      <span>1 Sample Road, Suite 100</span>
      <span>+1 555 010 0000</span>
      <span class="web">www.exwave.example</span>
    </div>
    <div class="page-num">Page 2 of 12</div>
  </section>

  <section class="page doc-summary">
    <div class="corner-brand"><span class="mark"></span>exWave</div>
    <div class="side-label" style="left:1px;top:117px">Document Summary</div>
    <h2 class="section-title" style="left:41px;top:68px">Document Summary</h2>
    <div class="body-copy" style="top:112px;line-height:12px">
      <p>This document is being provided to you, our valued customer, as a guided summary to enable the use of your environment effectively. Within the upcoming pages you will find helpful information pertaining to inventory, support team escalation procedures and contact information.</p>
      <p style="margin-top:3px">We welcome you to the next level of efficiency. To ensure (insert company name here) is running as proficient and robustly as possible we are happy to guide you down any necessary path. Your success is our vision.</p>
    </div>
  </section>

  <section class="page services">
    <div class="corner-brand"><span class="mark"></span>exWave</div>
    <div class="side-label" style="left:3px;top:72px">Services Summary</div>
    <h2 class="section-title" style="left:43px;top:56px">Services Summary</h2>
    <div class="body-copy" style="top:70px;line-height:14px">
      <p>The summary of services that exWave is supporting are listed below. Our goal is to assist you in clearly understanding these services. For information on how to use your services, please go to <a href="#">https://exwave.helpdesk.example/hc/en-us</a> or feel free to contact us directly for additional support.</p>
    </div>
    <ul class="service-list">
      <li>Hosted Mail</li>
      <li>Hosted Chat</li>
      <li>Hosted Servers</li>
      <li>Hosted email security with ShieldPoint Antivirus</li>
      <li>Server Backups</li>
      <li>Q7 Service Management System</li>
      <li>Hosted Team Portal</li>
      <li class="wrap">Assisted in terminal server configuration (supported during implementation – not a managed service)</li>
    </ul>
  </section>

</main>
</body>
</html>
```